Medical Billing Business needs a web page designed

We need a web page for a new medical billing business for prospective clients to go to to get information about our company. It needs to show what our company stands for and our billing rates. Our colors are blue, gray and white. I have attached our logo, brochure and mission statement.

Need tabs at top for "about us", "contact us" "specials". On contact page, need a form to fill out that will be automatically emailed to us upon completion. Under specials...Sign a contract by the end of August 2014 and receive one month of billing FREE. ***Receive 25% off the first 4 months of the contract***

Medical

```html
<!DOCTYPE html>
<html lang="en">
<head>
<meta charset="utf-8">
<title>Northfield Billing Co. – Medical Billing Business Services</title>
<link rel="stylesheet" href="https://fonts.googleapis.com/css2?family=Varela+Round&family=Open+Sans:wght@400;600&display=swap">
<style>
  :root {
    --brand-blue: #0d6d8f;
    --brand-blue-dark: #0a5674;
    --heading-blue: #1e6a99;
    --title-blue: #15587f;
    --rule-blue: #8aaac5;
    --text-gray: #6f6f6f;
    --body-gray: #555a5e;
    --heading-dark: #3a3d40;
    --accent-orange: #f39200;
    --frame-gray: #d6dbe0;
    --band-gray: #e6ebef;
    --white: #ffffff;
  }
  * { box-sizing: border-box; margin: 0; padding: 0; }
  html, body { width: 1107px; height: 1200px; overflow: hidden; background: var(--white); }
  body { position: relative; font-family: "Open Sans", Arial, sans-serif; color: var(--body-gray); }
  .abs { position: absolute; }

  .header-band {
    left: 0; top: 0; width: 1107px; height: 164px;
    background: linear-gradient(to bottom, #ffffff 0%, #ffffff 55%, #dfe7ee 100%);
  }
  .brand { left: 452px; top: 44px; display: flex; align-items: center; gap: 10px; }
  .brand-mark { width: 26px; height: 26px; background: var(--brand-blue); }
  .brand-name {
    font-family: "Varela Round", Arial, sans-serif; font-size: 21px;
    letter-spacing: 2px; color: var(--brand-blue-dark);
  }
  .social { left: 904px; top: 78px; display: flex; gap: 9px; }
  .social span { width: 22px; height: 22px; background: #3a76a8; display: block; }
  .social span:nth-child(2) { background: #5bbbe6; }
  .social span:nth-child(3) { background: #1f6fa4; }

  .main-nav {
    left: 105px; top: 114px; width: 891px; height: 50px;
    background: linear-gradient(to bottom, #1a86a8 0%, var(--brand-blue) 55%, var(--brand-blue-dark) 100%);
    border-radius: 3px 3px 0 0;
  }
  .main-nav a {
    position: absolute; top: 0; height: 50px; line-height: 50px;
    font-family: "Varela Round", Arial, sans-serif; font-size: 16px;
    color: var(--white); text-decoration: none; transform: translateX(-50%);
  }
  .nav-divider { position: absolute; top: 0; width: 1px; height: 50px; background: rgba(255,255,255,0.18); }

  .hero-frame { left: 105px; top: 164px; width: 891px; height: 392px; border: 1px solid var(--frame-gray); border-top: 0; background: var(--white); }
  .hero-photo {
    left: 171px; top: 164px; width: 784px; height: 392px;
    background: radial-gradient(ellipse at 40% 30%, #e9e4df 0%, #f1eeeb 40%, #e3e6ea 75%, #d9dde2 100%);
  }
  .hero-caption {
    left: 254px; top: 308px; width: 591px; height: 120px;
    background: rgba(255,255,255,0.82); border-radius: 3px; text-align: center;
  }
  .hero-title { font-family: "Varela Round", Arial, sans-serif; font-size: 32px; color: var(--title-blue); margin-top: 20px; }
  .hero-sub { font-family: "Varela Round", Arial, sans-serif; font-size: 20px; color: var(--heading-blue); margin-top: 2px; }
  .slider-dots { left: 527px; top: 537px; display: flex; gap: 3px; }
  .slider-dots span { width: 10px; height: 10px; border-radius: 50%; background: var(--title-blue); display: block; }

  .feature { top: 585px; width: 275px; }
  .feature-photo { width: 275px; height: 114px; border: 1px solid #cfd4d8; border-radius: 2px; }
  .feature h2 { font-family: "Varela Round", Arial, sans-serif; font-weight: 400; font-size: 24px; color: var(--heading-blue); margin-top: 9px; }
  .feature p { font-size: 12px; line-height: 18.5px; color: var(--text-gray); margin: 3px 0 0 2px; }
  .feature-rule { width: 275px; height: 3px; background: var(--rule-blue); margin-top: 17px; }

  .separator { left: 124px; top: 822px; width: 864px; height: 1px; background: #dde2e6; }

  .welcome { left: 110px; top: 860px; width: 440px; }
  .welcome h1 { font-family: "Varela Round", Arial, sans-serif; font-weight: 400; font-size: 22px; color: var(--heading-dark); }
  .welcome p { font-size: 11.3px; line-height: 17.5px; color: var(--body-gray); margin: 12px 0 0 2px; }
  .welcome p + p { margin-top: 9px; }

  .recent { left: 591px; top: 860px; width: 410px; }
  .recent h2 { font-family: "Varela Round", Arial, sans-serif; font-weight: 400; font-size: 23px; color: var(--accent-orange); }
  .post { display: flex; gap: 10px; margin-top: 15px; }
  .post + .post { margin-top: 21px; }
  .post-thumb { width: 72px; height: 57px; flex: none; }
  .post h3 { font-weight: 400; font-size: 13px; color: var(--heading-dark); margin-top: -3px; }
  .post p { font-size: 11.5px; line-height: 17.5px; color: var(--text-gray); margin-top: 4px; }

  .footer { left: 0; top: 1094px; width: 1107px; height: 106px; background: linear-gradient(to bottom, var(--band-gray), #eef1f4); }
  .footer-nav { position: absolute; left: 112px; top: 31px; font-family: "Varela Round", Arial, sans-serif; font-size: 14px; color: var(--title-blue); }
  .footer-nav a { color: var(--title-blue); text-decoration: none; }
  .footer-nav .pipe { margin: 0 9px; }
  .copyright { position: absolute; left: 112px; top: 64px; font-size: 11.5px; color: #7d8287; }
</style>
</head>
<body>
  <div class="abs header-band"></div>

  <div class="abs brand">
    <span class="brand-mark"></span>
    <span class="brand-name">NORTHFIELD BILLING CO.</span>
  </div>

  <div class="abs social" aria-label="Social links">
    <span></span><span></span><span></span>
  </div>

  <nav class="abs main-nav">
    <a href="#" style="left:214px">HOME</a>
    <span class="nav-divider" style="left:273px"></span>
    <a href="#" style="left:348px">ABOUT US</a>
    <span class="nav-divider" style="left:420px"></span>
    <a href="#" style="left:493px">SPECIALS</a>
    <span class="nav-divider" style="left:558px"></span>
    <a href="#" style="left:650px">CONTACT US</a>
  </nav>

  <div class="abs hero-frame"></div>
  <div class="abs hero-photo" role="img" aria-label="Photo of a smiling team of doctors and nurses in white coats"></div>
  <div class="abs hero-caption">
    <div class="hero-title">Medical Billing Business Services</div>
    <div class="hero-sub">Etiam est nunc venenatis tristique imperdiet</div>
  </div>
  <div class="abs slider-dots"><span></span><span></span><span></span><span></span></div>

  <section class="abs feature" style="left:107px">
    <div class="feature-photo" role="img" aria-label="Photo of a calculator and stethoscope on billing papers" style="background:linear-gradient(135deg,#b9c3cc,#e3e8ed 60%,#f3f5f7)"></div>
    <h2>What we do</h2>
    <p>Donec scelerisque leo ac risus Praesent sit amet est<br>In dictum dolor eu dictum porttitor enim</p>
    <div class="feature-rule"></div>
  </section>

  <section class="abs feature" style="left:413px">
    <div class="feature-photo" role="img" aria-label="Photo of an office worker reviewing medical bills" style="background:linear-gradient(135deg,#ececec,#d9d6d2 55%,#b8b4b0)"></div>
    <h2>Medical Bills</h2>
    <p>Donec scelerisque leo ac risus Praesent sit amet est<br>In dictum dolor eu dictum porttitor enim</p>
    <div class="feature-rule"></div>
  </section>

  <section class="abs feature" style="left:719px">
    <div class="feature-photo" role="img" aria-label="Photo of a smiling nurse in blue scrubs" style="background:linear-gradient(135deg,#5f8fa8,#b9a890 55%,#7fb3d6)"></div>
    <h2>Specials</h2>
    <p>Donec scelerisque leo ac risus Praesent sit amet est<br>In dictum dolor eu dictum porttitor enim</p>
    <div class="feature-rule"></div>
  </section>

  <div class="abs separator"></div>

  <section class="abs welcome">
    <h1>WELCOME TO NORTHFIELD WEBSITE</h1>
    <p>Vivamus porttitor g purus nisi eleifend libero a tempus libero lectus feugiat felis Morbi diam mauris viverra in gravida eu mattis in ante Morbi eget arcu Morbi porta libero id ullamcorper nonummy nibh ligula pulvinar metus eget consectetuer augue nisi quis lacus Ut ac mi quis lacus mollis aliquam</p>
    <p>Curabitur iaculis tempus eros Curabitur vel mi sit amet magna malesuada ultrices Ut nisi erat fermentum vel congue id euismod in elit Fusce ult</p>
  </section>

  <section class="abs recent">
    <h2>Recent Blog</h2>
    <article class="post">
      <div class="post-thumb" role="img" aria-label="Photo of two doctors reviewing a clipboard" style="background:linear-gradient(135deg,#cfd9e2,#f2f2f2 50%,#2d4f74)"></div>
      <div>
        <h3>Donec scelerisque leo</h3>
        <p>ultrices Ut nisi erat fermentum vel congue id euismod in elit Fusce ultricies orci ac feugiat suscipit leo</p>
      </div>
    </article>
    <article class="post">
      <div class="post-thumb" role="img" aria-label="Photo of a doctor with an elderly patient" style="background:linear-gradient(135deg,#e9d8c6,#f4f1ee 50%,#b9c7d6)"></div>
      <div>
        <h3>Nunc porta convallis pede</h3>
        <p>ultrices Ut nisi erat fermentum vel congue id euismod in elit Fusce ultricies orci ac feugiat suscipit leo</p>
      </div>
    </article>
  </section>

  <footer class="abs footer">
    <div class="footer-nav">
      <a href="#">HOME</a><span class="pipe">|</span><a href="#">ABOUT US</a><span class="pipe">|</span><a href="#">SPECIALS</a><span class="pipe">|</span><a href="#">CONTACT US</a>
    </div>
    <div class="copyright">© 2014 Company Name.&nbsp; All right reserved.&nbsp; Term of Use</div>
  </footer>
</body>
</html>
```